Cosmetic injections clinic needs a fresh looking business card

We need a business card using the supplied logo and color scheme to attract future clients to our clinic. It should be modern and fresh, eye catching and not too busy. Simple and to the point is best. I would like two sided designs with the front indicating address and contact information, and the back in full color with white logo and descriptive information also provided.
Target Market(s)
Clients looking for non surgical beauty enhancements.
Contact Information for Business Card
MeloraSkin
14, 618 Birchmont Way
St. Albert, Alberta
K2P 7W3
Phone: 587-412-6630
Email: info@meloraskin.com
Requirements
Must have
- -Logo supplied with the name and address of the clinic
- -Back of card in full color with white logo with A small line of text indicating both of the following: Anti aging consultants and cosmetic injectables
- Located inside the Voyager Wellness Group

```html
<!DOCTYPE html>
<html lang="en">
<head>
<meta charset="utf-8">
<title>MeloraSkin – Business Card</title>
<link rel="stylesheet" href="https://fonts.googleapis.com/css2?family=Lato:wght@400;700&family=Montserrat:wght@600;800&display=swap">
<style>
  :root {
    --stage: #3a3a3c;
    --paper: #ffffff;
    --ink: #2b2b2b;
    --pink: #e0409a;
    --purple: #6b3fa0;
    --teal: #2fbfa3;
    --white: #ffffff;
  }
  * { box-sizing: border-box; margin: 0; padding: 0; }
  html, body { width: 1200px; height: 782px; overflow: hidden; }
  body {
    background: var(--stage);
    display: flex;
    align-items: center;
    justify-content: center;
    gap: 40px;
    font-family: "Lato", sans-serif;
  }
  .card {
    position: relative;
    width: 560px;
    height: 320px;
    overflow: hidden;
    box-shadow: 0 10px 30px rgba(0,0,0,.45);
  }

  .wordmark {
    position: absolute;
    display: flex; align-items: center; gap: 10px;
    white-space: nowrap;
  }
  .wordmark__dot { width: 24px; height: 24px; border-radius: 50%; flex: none; }
  .wordmark__name {
    font-family: "Montserrat", sans-serif; font-weight: 800;
    font-size: 28px; letter-spacing: .5px; line-height: 1;
  }

  /* Front */
  .card--front { background: var(--paper); color: var(--ink); }
  .contact {
    position: absolute; left: 34px; top: 34px;
    list-style: none; font-size: 15px; line-height: 1.45;
  }
  .contact li { display: flex; align-items: center; gap: 7px; }
  .contact svg { width: 13px; height: 13px; fill: var(--pink); flex: none; }
  .address {
    position: absolute; left: 34px; top: 118px; width: 250px;
    font-style: normal; font-size: 15px; line-height: 1.3;
  }
  .address .clinic { color: var(--pink); letter-spacing: .5px; }
  .card--front .wordmark { right: 28px; top: 160px; }
  .card--front .wordmark__dot { background: var(--purple); }
  .card--front .wordmark__name { color: var(--purple); }
  .waves { position: absolute; left: 0; bottom: 0; width: 560px; height: 140px; }

  /* Back */
  .card--back {
    background: linear-gradient(170deg, var(--pink) 0%, #b05aa8 18%, var(--teal) 50%, #3f9fa8 72%, var(--purple) 100%);
    color: var(--white);
  }
  .card--back .wordmark { left: 40px; top: 146px; }
  .card--back .wordmark__dot { background: var(--white); }
  .card--back .wordmark__name { color: var(--white); font-size: 26px; }
  .services {
    position: absolute; left: 300px; top: 120px; width: 240px;
    list-style: none;
    font-family: "Montserrat", sans-serif; font-weight: 800;
    font-size: 12.5px; line-height: 1.35; text-transform: uppercase; letter-spacing: .3px;
  }
  .services li { position: relative; padding-left: 12px; margin-bottom: 6px; }
  .services li::before {
    content: ""; position: absolute; left: 0; top: 5px;
    width: 6px; height: 6px; border-radius: 50%; background: var(--white);
  }
</style>
</head>
<body>

  <section class="card card--front" aria-label="Business card front">
    <ul class="contact">
      <li>
        <svg viewBox="0 0 24 24" aria-hidden="true"><path d="M6.6 10.8a15.1 15.1 0 0 0 6.6 6.6l2.2-2.2c.3-.3.7-.4 1-.2 1.1.4 2.3.6 3.6.6.6 0 1 .4 1 1V20c0 .6-.4 1-1 1A17 17 0 0 1 3 4c0-.6.4-1 1-1h3.5c.6 0 1 .4 1 1 0 1.3.2 2.5.6 3.6.1.3 0 .7-.2 1z"/></svg>
        587-412-6630
      </li>
      <li>
        <svg viewBox="0 0 24 24" aria-hidden="true"><path d="M2 5h20v14H2zm2 2v.5l8 5 8-5V7l-8 5z"/></svg>
        info@meloraskin.com
      </li>
    </ul>

    <address class="address">
      <span class="clinic">MELORASKIN</span><br>
      14, 618 Birchmont Way St. Albert<br>
      Alberta&nbsp; K2P 7W3
    </address>

    <div class="wordmark">
      <span class="wordmark__dot"></span>
      <span class="wordmark__name">MELORASKIN</span>
    </div>

    <svg class="waves" viewBox="0 0 560 140" preserveAspectRatio="none" aria-hidden="true">
      <path d="M0 38 C120 60 240 110 360 118 C430 122 500 100 560 80 L560 140 L0 140 Z" fill="var(--teal)"/>
      <path d="M0 30 C140 56 260 112 380 122 C450 128 510 124 560 118 L560 140 L0 140 Z" fill="var(--white)"/>
      <path d="M0 44 C140 66 260 118 390 128 C460 134 520 132 560 130 L560 140 L0 140 Z" fill="var(--pink)"/>
      <path d="M0 10 C90 28 200 70 330 92 C250 74 120 40 0 22 Z" fill="var(--purple)"/>
    </svg>
  </section>

  <section class="card card--back" aria-label="Business card back">
    <div class="wordmark">
      <span class="wordmark__dot"></span>
      <span class="wordmark__name">MELORASKIN</span>
    </div>
    <ul class="services">
      <li>Anti aging consultants and cosmetic injectables</li>
      <li>Located inside the Voyager Wellness Group</li>
    </ul>
  </section>

</body>
</html>
```